Criação de Kit Layout de Posts para Redes Sociais (Facebook, Instagram e etc) para Tecnologia & Ciencias
A empresa queria:
" DESENVOLVE, IMPLANTA O SOFTWARE E DA SUPORTE (AO CLIENTE). "

```html
<!DOCTYPE html>
<html lang="pt-BR">
<head>
<meta charset="utf-8">
<title>NovaByte Sistemas – Restaurantes</title>
<link href="https://fonts.googleapis.com/css2?family=Oswald:wght@400;500;600&display=swap" rel="stylesheet">
<style>
  :root {
    --orange: #f39a1e;
    --white: #ffffff;
    --ink: #1c1612;
    --photo-dark: #2a1f18;
    --photo-mid: #6b5344;
    --photo-warm: #b48a6a;
  }
  html, body {
    margin: 0;
    padding: 0;
    width: 1200px;
    height: 1200px;
    overflow: hidden;
    background: var(--ink);
  }
  .post {
    position: relative;
    width: 1200px;
    height: 1200px;
    overflow: hidden;
    font-family: "Oswald", "Arial Narrow", sans-serif;
    color: var(--white);
  }
  .post__photo {
    position: absolute;
    inset: 0;
    background:
      radial-gradient(ellipse 420px 520px at 720px 640px, rgba(214,170,140,0.55), transparent 70%),
      radial-gradient(ellipse 380px 300px at 900px 260px, rgba(160,120,90,0.45), transparent 70%),
      radial-gradient(ellipse 360px 460px at 260px 520px, rgba(90,70,60,0.7), transparent 70%),
      linear-gradient(160deg, var(--photo-dark) 0%, var(--photo-mid) 45%, var(--photo-warm) 70%, var(--photo-dark) 100%);
  }
  .post__shade {
    position: absolute;
    inset: 0;
    background: linear-gradient(180deg, transparent 0%, transparent 70%, rgba(20,14,10,0.85) 90%, rgba(20,14,10,0.95) 100%);
  }
  .brand {
    position: absolute;
    top: 64px;
    left: 648px;
    display: flex;
    align-items: center;
    gap: 20px;
  }
  .brand__mark {
    width: 118px;
    height: 118px;
    border-radius: 50%;
    background: var(--orange);
  }
  .brand__text {
    display: flex;
    flex-direction: column;
    align-items: flex-end;
  }
  .brand__name {
    font-size: 76px;
    font-weight: 600;
    line-height: 1;
    color: var(--white);
    letter-spacing: 2px;
  }
  .brand__tag {
    font-size: 26px;
    font-weight: 400;
    line-height: 1;
    color: var(--orange);
    letter-spacing: 3px;
    margin-top: 4px;
  }
  .headline {
    position: absolute;
    left: 48px;
    top: 474px;
    margin: 0;
    text-transform: uppercase;
    line-height: 1.14;
    font-weight: 400;
  }
  .headline__line { display: block; }
  .headline__accent {
    color: var(--orange);
    font-size: 70px;
    font-weight: 500;
    letter-spacing: 8px;
  }
  .headline__body {
    color: var(--white);
    font-size: 56px;
    letter-spacing: 6px;
  }
  .social {
    position: absolute;
    left: 864px;
    top: 1010px;
    display: flex;
    gap: 22px;
  }
  .social__dot {
    width: 44px;
    height: 44px;
    border-radius: 50%;
    background: var(--white);
  }
  .contact {
    position: absolute;
    top: 1082px;
    display: flex;
    align-items: center;
    gap: 22px;
    font-size: 17px;
    line-height: 1.3;
    font-weight: 400;
    color: var(--white);
  }
  .contact--phone { left: 96px; }
  .contact--web { left: 466px; }
  .contact--address { left: 864px; }
  .contact__icon {
    width: 54px;
    height: 54px;
    flex: none;
  }
</style>
</head>
<body>
  <main class="post">
    <div class="post__photo" role="img" aria-label="Fotografia de dois atendentes de restaurante de avental sorrindo enquanto usam um notebook em uma cozinha"></div>
    <div class="post__shade"></div>

    <div class="brand">
      <div class="brand__mark"></div>
      <div class="brand__text">
        <span class="brand__name">NovaByte</span>
        <span class="brand__tag">Sistemas</span>
      </div>
    </div>

    <h1 class="headline">
      <span class="headline__line headline__accent">Restaurantes</span>
      <span class="headline__line headline__body">Desenvolvimento,</span>
      <span class="headline__line headline__body">Implantação</span>
      <span class="headline__line headline__body">e suporte de</span>
      <span class="headline__line headline__accent">Software</span>
    </h1>

    <div class="social">
      <div class="social__dot"></div>
      <div class="social__dot"></div>
    </div>

    <div class="contact contact--phone">
      <svg class="contact__icon" viewBox="0 0 54 54" aria-hidden="true">
        <rect x="1" y="1" width="52" height="52" rx="10" fill="#ffffff"/>
        <path d="M19 14c2 0 3 4 4 6s-2 3-1 5 5 7 8 8 3-2 5-1 6 2 6 4-3 5-6 5C24 41 13 30 13 20c0-3 3-6 6-6z" fill="#1c1612"/>
      </svg>
      <div>+55 (11) 99999-9999<br>+55 (11) 9999-9999</div>
    </div>

    <div class="contact contact--web">
      <svg class="contact__icon" viewBox="0 0 54 54" aria-hidden="true">
        <circle cx="27" cy="27" r="26" fill="#ffffff"/>
        <g fill="none" stroke="#1c1612" stroke-width="2.5">
          <circle cx="27" cy="27" r="15"/>
          <ellipse cx="27" cy="27" rx="7" ry="15"/>
          <line x1="12" y1="27" x2="42" y2="27"/>
          <path d="M15 19h24M15 35h24"/>
        </g>
      </svg>
      <div>email@seuemail.com.br<br>www.site.com.br</div>
    </div>

    <div class="contact contact--address">
      <svg class="contact__icon" viewBox="0 0 54 54" aria-hidden="true">
        <rect x="1" y="1" width="52" height="52" rx="8" fill="#ffffff"/>
        <path d="M27 11c-7 0-12 5-12 12 0 9 12 21 12 21s12-12 12-21c0-7-5-12-12-12zm0 17a5 5 0 1 1 0-10 5 5 0 0 1 0 10z" fill="#1c1612"/>
      </svg>
      <div>Rua Exemplo de Nome, 1111<br>Bairro Nome do Bairro<br>88888-000 - São Paulo / SP</div>
    </div>
  </main>
</body>
</html>
```